ebook cover: book 4 in the We Hum Lantern series. Lantern by Riverside

I am wanting a striking cover to bring the forth book in a spiritual journey series to an audience ready to meet new characters and get excited again! White backgrounds, red titles (any font), subtitles to introduce a new major character in the series of ten (same fonts please as the original, We Hum Lantern), and one emblematic, slightly mysterious image. Please keep to the same colour tones as the original, but the lead image need not be gray. Let's please try to use the "light flash" that is on the tin can in We Hum Lantern somehow, in your own way. It is meant to signify the other side, or the higher light, or some such inference.

Book details:
Title: Lantern by Riverside
Subtitle: Archangel Veloriel brings the message
Image: silver hourglass
Author: Maren Tulliver, Ph.D
Strap quote: "Tulliver is smart, savvy and full of ideas," Harbourgate Ledger

Please do your best: this one is going in competition of spiritual healers!

Thanks! :)

```html
<!DOCTYPE html>
<html lang="en">
<head>
<meta charset="UTF-8">
<title>Lantern by Riverside – Book Cover</title>
<link href="https://fonts.googleapis.com/css2?family=Bebas+Neue&family=Open+Sans:wght@400;600;700&display=swap" rel="stylesheet">
<style>
  :root {
    --stage: #2f2f2f;
    --paper: #ffffff;
    --title-red-light: #e0262b;
    --title-red-dark: #b30f16;
    --ink: #2b2b2b;
    --ink-soft: #3a3a3a;
    --silver-light: #f4f4f4;
    --silver-mid: #c9c9c9;
    --silver-dark: #8e8e8e;
  }
  * { margin: 0; padding: 0; box-sizing: border-box; }
  html, body {
    width: 1200px;
    height: 1200px;
    overflow: hidden;
    background: var(--stage);
  }
  .canvas {
    position: relative;
    width: 1200px;
    height: 1200px;
    display: flex;
    align-items: center;
    justify-content: center;
  }
  .cover {
    position: relative;
    width: 740px;
    height: 1110px;
    background: var(--paper);
    display: flex;
    flex-direction: column;
    align-items: center;
    box-shadow: 0 20px 50px rgba(0,0,0,0.45);
  }
  .strap-quote {
    margin-top: 58px;
    text-align: center;
    font-family: "Open Sans", sans-serif;
    font-weight: 600;
    font-size: 27px;
    line-height: 1.2;
    letter-spacing: -0.3px;
    color: var(--ink-soft);
    text-transform: uppercase;
  }
  .strap-quote .source { display: block; }
  .title {
    margin-top: 20px;
    font-family: "Bebas Neue", sans-serif;
    font-weight: 400;
    font-size: 178px;
    line-height: 0.86;
    text-align: center;
    text-transform: uppercase;
    letter-spacing: 1px;
    background: linear-gradient(180deg, var(--title-red-light) 0%, var(--title-red-dark) 100%);
    -webkit-background-clip: text;
    background-clip: text;
    color: transparent;
  }
  .title span { display: block; }
  .subtitle {
    margin-top: 14px;
    font-family: "Open Sans", sans-serif;
    font-weight: 600;
    font-size: 31px;
    color: var(--ink);
    text-align: center;
  }
  .lead-image {
    margin-top: 34px;
    width: 270px;
    height: 470px;
    border-radius: 18px;
    background:
      radial-gradient(ellipse at 50% 45%, var(--silver-light) 0%, var(--silver-mid) 60%, var(--silver-dark) 100%);
  }
  .author {
    margin-top: auto;
    margin-bottom: 62px;
    font-family: "Open Sans", sans-serif;
    font-weight: 400;
    font-size: 28px;
    letter-spacing: 4px;
    color: var(--ink);
    text-transform: uppercase;
  }
  .author .credential {
    font-variant: small-caps;
    text-transform: none;
    font-size: 30px;
  }
</style>
</head>
<body>
  <main class="canvas">
    <article class="cover">
      <p class="strap-quote">
        “Tulliver is smart, savvy and full of ideas,”
        <span class="source">- Harbourgate Ledger</span>
      </p>
      <h1 class="title">
        <span>Lantern by</span>
        <span>Riverside</span>
      </h1>
      <p class="subtitle">Archangel Veloriel brings the message</p>
      <div class="lead-image" role="img" aria-label="Silver hourglass with white sand standing in a polished metal frame"></div>
      <p class="author">Maren Tulliver <span class="credential">Ph.D.</span></p>
    </article>
  </main>
</body>
</html>
```